BRIGHTDESK - Remote Tech Support Site

We are looking for a new very responsive and simple website for our brand Brightdesk.com - a remote technical support company.

This company supports customers Globally in different countries throughout Eur/ North America / South America / Asia etc (please keep this in mind and integrate into the idea).

Its important to us that the design is very explanatory, the customer should easily be able to figure out that we provide computer support right away ... I like one page responsive type designs as well without a bunch of menu items

Here are some similar sites we like - but still looking for a unique design that fits out brand "brightdesk" - I have upload also some layouts i like (but the designs are not important just the layouts), youll see it includes consumer business etc which is important.

VOLM.COM - I love how clean it is - nice and white easy to see everything

PLUMWIRE247.COM - also nice the layout and responsive one page design makes it easy to use

corvalfix.com - similar to plumwire design as well - you can get the idea im looking for between the two

You will notice those examples are much different then the attachments I added - again this is more of an idea for possible layouts .. attached is also the logo - could inspire color scheme / blue white black etc

Target Market(s)

Home consumers without computer knowledge , older age 45-65, small medium business ... computer repair - slow computers

Industry/Entity Type

Computer Repair

Logo Text

Brightdesk

Coding

Coded - Design and coding required

Number of Pages Required

1 page

Font styles to use
Sans Serif
Other font styles liked:
• your choice responsive

Colors

Designer to choose colors to be used in the design.

Requirements
Must have
• Clean - responsive - professional design - the name says it all - brightdesk
• CALL TO ACTIONS FOR "Get Help Now!" / "Learn More" etc
Nice to have
• We are looking for a new very responsive and simple website for our brand Brightdesk.com - a remote technical support company.
• This company supports customers Globally in different countries throughout Eur/ North America / South America / Asia etc (please keep this in mind and integrate into the idea).
• Its important to us that the design is very explanatory, the customer should easily be able to figure out that we provide computer support right away ... I like one page responsive type designs as well without a bunch of menu items
• Here are some similar sites we like - but still looking for a unique design that fits out brand "brightdesk" - I have upload also some layouts i like (but the designs are not important just the layouts), youll see it includes consumer business etc which is important.
• VOLM.COM - I love how clean it is - nice and white easy to see everything
• PLUMWIRE247.COM - also nice the layout and responsive one page design makes it easy to use
• corvalfix.com - similar to plumwire design as well - you can get the idea im looking for between the two
Should not have
• dark, packed page - bad small font -

```html
<!DOCTYPE html>
<html lang="en">
<head>
<meta charset="utf-8">
<title>Brightdesk – Remote Tech Support</title>
<link href="https://fonts.googleapis.com/css2?family=Montserrat:wght@300;400;500;600&family=Roboto:wght@300;400&display=swap" rel="stylesheet">
<style>
:root{
  --ink:#1d1d1f;
  --muted:#555;
  --accent:#1c3fd6;
  --panel-gray:#cfcfcf;
  --plan-dark:#3f7fa6;
  --plan-blue:#3b95d3;
  --page:#ffffff;
  --footer:#f6f6f6;
  --white:#ffffff;
}
*{margin:0;padding:0;box-sizing:border-box}
html,body{width:1200px;height:3838px;overflow:hidden}
body{position:relative;background:var(--page);font-family:"Montserrat",sans-serif;color:var(--ink)}
.abs{position:absolute}

/* nav */
.site-nav{left:0;top:0;width:1200px;height:72px}
.brand{left:46px;top:31px;font-size:13px;font-weight:600;letter-spacing:1.5px}
.nav-links{right:38px;top:34px;display:flex;gap:28px;font-size:10px;font-weight:600;letter-spacing:2px}

/* hero */
.hero-photo{left:0;top:72px;width:1185px;height:755px;background:linear-gradient(100deg,#6d747a 0%,#b9c3cb 35%,#dfe6ec 60%,#c9d2da 100%)}
.hero-card{left:72px;top:256px;width:542px;height:384px;background:rgba(255,255,255,.82)}
.hero-icon{left:61px;top:77px}
.hero-title{left:53px;top:202px;font-size:22px;font-weight:400;letter-spacing:6px;line-height:34px}
.hero-sub{left:53px;top:274px;font-family:"Roboto",sans-serif;font-size:9px;letter-spacing:.6px;color:var(--muted)}
.btn{display:flex;align-items:center;justify-content:center;background:var(--accent);color:var(--white);font-weight:600;letter-spacing:1.5px;border-radius:30px}
.hero-btn{left:53px;top:312px;width:133px;height:22px;font-size:7px}

/* steps */
.section-label{font-size:18px;font-weight:400;letter-spacing:4px}
.steps-label{left:154px;top:884px}
.step-block{left:161px;top:972px;width:878px;height:384px;background:var(--panel-gray)}
.step-photo{left:0;top:0;width:448px;height:384px;background:linear-gradient(135deg,#8e96a0 0%,#c7cbd0 45%,#e8e8e6 100%)}
.step-num{left:484px;top:110px;font-size:11px;letter-spacing:2px;color:#666}
.step-title{left:484px;top:134px;font-size:14px;font-weight:500;letter-spacing:3px}
.step-text{left:484px;top:175px;width:360px;font-family:"Roboto",sans-serif;font-size:12px;line-height:19px;color:#666}
.step-btn{left:484px;top:231px;width:143px;height:46px;font-size:12px;border-radius:24px}

/* features */
.center{left:0;width:1200px;text-align:center}
.features-title{top:1428px;font-size:30px;font-weight:400;letter-spacing:4px}
.features-sub{top:1482px;font-family:"Roboto",sans-serif;font-size:13px;color:#777}
.feature{width:205px}
.feature svg{display:block;height:24px}
.feature h3{margin-top:20px;font-size:17px;font-weight:400;letter-spacing:2.5px}
.feature .dash{width:18px;border-top:2px solid var(--ink);margin-top:28px}
.feature p{margin-top:12px;font-family:"Roboto",sans-serif;font-size:11px;line-height:17px;color:#444}
.feature.tall h3{line-height:26px}

/* trusted */
.trusted-title{top:2080px;font-size:17px;letter-spacing:4px}
.badge{top:2162px}

/* pricing */
.plan-title{top:2356px;font-size:28px;font-weight:400;letter-spacing:5px}
.plan-sub{top:2408px;font-size:16px;color:#777}
.plan-note{top:2436px;font-family:"Roboto",sans-serif;font-size:10px;color:#222}
.plans{left:161px;top:2472px;width:878px;height:397px;display:flex}
.plan{flex:1;color:var(--white);text-align:center;padding-top:42px;background:var(--plan-blue)}
.plan + .plan{border-left:2px solid var(--white)}
.plan.dark{background:var(--plan-dark)}
.plan h4{font-size:18px;font-weight:400;letter-spacing:2px}
.plan .rule{width:82px;border-top:1px solid rgba(255,255,255,.7);margin:30px auto 0}
.plan .price{margin-top:22px;font-size:29px;line-height:34px}
.plan ul{list-style:none;margin-top:18px;font-family:"Roboto",sans-serif;font-size:11px;font-weight:400;line-height:15px;height:70px}
.plan .more{display:inline-flex;align-items:center;justify-content:center;width:110px;height:44px;background:var(--white);color:var(--plan-dark);border-radius:24px;font-family:"Roboto",sans-serif;font-size:10px}

/* closing band */
.closing-photo{left:0;top:2897px;width:1200px;height:445px;background:linear-gradient(180deg,#4a4a4a 0%,#7b7b7b 55%,#5c5c5c 100%)}
.closing-text{left:328px;top:3078px;width:560px;color:var(--white);font-size:15px;letter-spacing:3.5px;line-height:21px}
.page-foot{left:0;top:3342px;width:1200px;height:496px;background:var(--footer)}
</style>
</head>
<body>

<header class="abs site-nav">
  <div class="abs brand">BRIGHTDESK</div>
  <nav class="abs nav-links"><span>HOW TO</span><span>FEATURES</span><span>PRICING</span></nav>
</header>

<section>
  <div class="abs hero-photo" role="img" aria-label="Photo of a smiling support technician in a striped shirt at his desk"></div>
  <div class="abs hero-card">
    <svg class="abs hero-icon" width="72" height="92" viewBox="0 0 72 92" aria-hidden="true">
      <path d="M12 40a24 24 0 0 1 48 0" fill="none" stroke="#000" stroke-width="6"/>
      <rect x="4" y="36" width="14" height="24" rx="5" fill="#000"/>
      <rect x="54" y="36" width="14" height="24" rx="5" fill="#000"/>
      <path d="M60 58q0 14-18 16" fill="none" stroke="#000" stroke-width="4"/>
      <path d="M6 92v-14q0-12 30-12t30 12v14z" fill="#000"/>
      <circle cx="36" cy="82" r="2.5" fill="#fff"/>
    </svg>
    <h1 class="abs hero-title">DEDICATED SUPPORT<br>ANYTIME. ANYWHERE.</h1>
    <p class="abs hero-sub">BRIGHTDESK IS YOUR OWN PC SUPPORT TEAM, AVAILABLE ANYTIME, ANYWHERE</p>
    <a class="abs btn hero-btn">GET SUPPORT NOW</a>
  </div>
</section>

<section>
  <h2 class="abs section-label steps-label">HOW IT WORKS IN 3 STEPS</h2>
  <div class="abs step-block">
    <div class="abs step-photo" role="img" aria-label="Photo of a desktop monitor showing an online security scan"></div>
    <div class="abs step-num">STEP 1</div>
    <div class="abs step-title">FREE DIAGNOSTIC</div>
    <p class="abs step-text">Get a diagnostic for FREE! Receive a free consultation session with our staff.</p>
    <a class="abs btn step-btn">GET SUPPORT</a>
  </div>
</section>

<section>
  <h2 class="abs center features-title">The Best Features</h2>
  <p class="abs center features-sub">At the Best Price!</p>

  <div class="abs feature" style="left:161px;top:1596px">
    <svg width="14" viewBox="0 0 14 24" aria-hidden="true"><rect x="2" y="2" width="10" height="20" rx="2" fill="none" stroke="#333" stroke-width="1.5"/></svg>
    <h3>Mobile Security</h3><div class="dash"></div><p>Coming Soon!</p>
  </div>
  <div class="abs feature" style="left:389px;top:1596px">
    <svg width="20" viewBox="0 0 20 24" aria-hidden="true"><rect x="3" y="11" width="14" height="11" rx="1" fill="none" stroke="#333" stroke-width="1.5"/><path d="M6 11V7a4 4 0 0 1 8 0v4" fill="none" stroke="#333" stroke-width="1.5"/></svg>
    <h3>Identity Protection</h3><div class="dash"></div><p>Coming Soon!</p>
  </div>
  <div class="abs feature" style="left:617px;top:1596px">
    <svg width="28" viewBox="0 0 28 24" aria-hidden="true"><path d="M14 2 26 8 14 14 2 8z M2 13l12 6 12-6 M2 18l12 6 12-6" fill="none" stroke="#333" stroke-width="1.5"/></svg>
    <h3>Multiple Devices</h3><div class="dash"></div><p>Get support for up to 4 multiple devices. Add more per family plans.</p>
  </div>
  <div class="abs feature" style="left:845px;top:1596px">
    <svg width="30" viewBox="0 0 30 24" aria-hidden="true"><rect x="2" y="2" width="26" height="20" fill="none" stroke="#333" stroke-width="1.5"/><path d="M8 18v-6M13 18V8M18 18v-8M23 18V6" stroke="#333" stroke-width="2.5"/></svg>
    <h3>System Reports</h3><div class="dash"></div><p>Comes to date with Realtime system reporting.</p>
  </div>

  <div class="abs feature" style="left:161px;top:1826px">
    <svg width="22" viewBox="0 0 22 24" aria-hidden="true"><rect x="2" y="5" width="18" height="12" fill="none" stroke="#333" stroke-width="1.5"/><path d="M8 21h6M11 17v4" stroke="#333" stroke-width="1.5"/></svg>
    <h3>Regular Tune-ups</h3><p style="margin-top:38px">Get regular tune-ups to ensure fast speed every 90 days.</p>
  </div>
  <div class="abs feature" style="left:389px;top:1826px">
    <svg width="22" viewBox="0 0 22 24" aria-hidden="true"><circle cx="11" cy="12" r="8" fill="none" stroke="#333" stroke-width="1.5"/><circle cx="11" cy="12" r="2.5" fill="none" stroke="#333" stroke-width="1.5"/></svg>
    <h3>Ad Blocker</h3><p style="margin-top:38px">Avoid annoying pop-ups with the newest Ad-Blocking technology.</p>
  </div>
  <div class="abs feature tall" style="left:617px;top:1826px">
    <svg width="26" viewBox="0 0 26 24" aria-hidden="true"><rect x="3" y="8" width="14" height="14" fill="none" stroke="#333" stroke-width="1.5"/><path d="M8 8V3h15v14h-6" fill="none" stroke="#333" stroke-width="1.5"/></svg>
    <h3>Cross Platform<br>Support</h3><p style="margin-top:22px">Get support for all different types of devices.</p>
  </div>
  <div class="abs feature" style="left:845px;top:1826px">
    <svg width="30" viewBox="0 0 30 24" aria-hidden="true"><path d="M8 20a6 6 0 0 1 0-12 8 8 0 0 1 15 2 5 5 0 0 1 0 10z" fill="#333"/><path d="M15 17v-6M12 13l3-3 3 3" stroke="#fff" stroke-width="1.8" fill="none"/></svg>
    <h3>Cloud Backup</h3><p style="margin-top:38px">Backup your valuable data to a secure cloud backup.</p>
  </div>
</section>

<section>
  <h2 class="abs center trusted-title">TRUSTED BY:</h2>
  <div class="abs badge" style="left:240px;top:2176px;width:108px;height:44px;background:#2f9a63;border-radius:3px" role="img" aria-label="Review site badge"></div>
  <div class="abs badge" style="left:548px;width:104px;height:76px;background:#d8262c;border-radius:50%" role="img" aria-label="Secure site badge"></div>
  <div class="abs badge" style="left:860px;width:80px;height:76px;background:#c99a24;border-radius:50%" role="img" aria-label="Satisfaction guarantee badge"></div>
</section>

<section>
  <h2 class="abs center plan-title">CHOOSE YOUR PLAN</h2>
  <p class="abs center plan-sub">Easy Monthly Pricing</p>
  <p class="abs center plan-note">(all plans come with a $29.99 setup fee)</p>
  <div class="abs plans">
    <div class="plan dark">
      <h4>Premium</h4><div class="rule"></div>
      <div class="price">$19.99<br>Monthly</div>
      <ul><li>Regular 90 Day Optimization</li><li>Unlimited 24/7 Tier 3</li><li>Technician Support</li></ul>
      <a class="more">Learn More</a>
    </div>
    <div class="plan">
      <h4>Premium Plus</h4><div class="rule"></div>
      <div class="price">$29.99<br>Monthly</div>
      <ul><li>Regular 60 Day Optimization</li><li>Unlimited 24/7 Tier 3</li><li>Technician Support</li></ul>
      <a class="more">Learn More</a>
    </div>
    <div class="plan">
      <h4>Platinum</h4><div class="rule"></div>
      <div class="price">$39.99<br>Monthly</div>
      <ul><li>Regular 30 Day Optimization</li><li>Unlimited 24/7 Tier 3</li><li>Technician Support</li><li>Online Identity Theft Protection</li></ul>
      <a class="more">Learn More</a>
    </div>
  </div>
</section>

<section>
  <div class="abs closing-photo" role="img" aria-label="Black and white photo of a person relaxing with a laptop"></div>
  <p class="abs closing-text">BRIGHTDESK IS YOUR OWN PC TECHNICAL TEAM AVAILABLE TO YOU 24/7 YOU NEED NOT WORRY ANYMORE ABOUT PC COMPLICATIONS. SIT BACK IN THE COMFORT OF KNOWING THAT EXPERT SUPPORT IS JUST A CLICK AWAY.</p>
  <div class="abs page-foot"></div>
</section>

</body>
</html>
```